An innovative, creative health promotion project needs you to add spice to logo and web design!

Wellorivan is “medical education for Asians”. We work with people from Indian, Pakistani, Bangladeshi and Sri Lankan backgrounds based in the UK. The aim is to use all of the great things we celebrate about Indian culture such as the vibrant colour, fashion, music, dance, Bollywood, cricket, tasty food and close family networks and use this to improve awareness about healthy living. Our tagline is “bright days with a little zest”. We are a group of healthcare professionals and creatives working in collaboration and we produce video interviews, local community events, blog posts and social media to address issues such as diabetes, heart disease, depression. We have 3 main subcategories – Mind, Movement and Meals. “Mind” addresses issues around mental illness through interviews with patients and healthcare professionals. “Movement” will get people more physically active through video and local group exercise and walking meetings. “Meals” will feature recipes from renowned Asian chefs to provide healthier alternatives. So far I have designed an amateur logo and we have a facebook page https://www.friendnook.example/wellorivan/ and a website hosted on wordpress: https://wellorivan.org/We are looking at help to create a simple but effective web design, logos and colour scheme that will capture the vibrant culture and give a feeling of energy, health and fun!

Target Market(s)

UK Indian community, all ages

Industry/Entity Type

Healthcare

Logo Text

bright days with a little zest

Number of Pages Required

1 page

Font styles to use
Sans Serif

Colors

Designer to choose colors to be used in the design.

Requirements
Must have
• Colour, vibrancy, energy, spice! fun!
Nice to have
• I would like clean design with ethnic colours.
Should not have
• No religious graphics

```html
<!DOCTYPE html>
<html lang="en">
<head>
<meta charset="utf-8">
<title>Wellorivan – bright days with a little zest</title>
<link href="https://fonts.googleapis.com/css2?family=Montserrat:wght@300;400;500;600;700&display=swap" rel="stylesheet">
<style>
:root{
  --canvas:#ebebeb; --white:#fff; --teal:#00a69a; --mint:#80c7a3; --mint-dark:#64a884;
  --ink:#111; --grey:#888; --card:#ececec; --light:#f2f2f2; --footer:#141414;
  --orange:#f7931e; --navy:#2e3192; --green:#1d9a4a; --red:#a3162b;
}
*{margin:0;padding:0;box-sizing:border-box}
html,body{width:1200px;height:1200px;overflow:hidden;background:var(--canvas);font-family:'Montserrat',sans-serif;color:var(--ink)}
.page{position:absolute;width:560px;background:var(--white);overflow:hidden}
.page--left{left:27px;top:80px;height:1120px}
.page--right{left:611px;top:0;height:1120px}
.abs{position:absolute}
.nav{left:0;top:0;width:560px;height:53px}
.brand{left:58px;top:17px;font-size:14px;font-weight:700;color:var(--teal)}
.nav-links{left:170px;top:22px;display:flex;gap:17px;font-size:7.2px;color:#333}
.hero{left:0;top:53px;width:560px;height:233px;background:linear-gradient(120deg,#4a4542,#3b3436 45%,#5a3a4a 70%,#2f2c2c)}
.hero h1{position:absolute;left:0;width:560px;top:76px;text-align:center;font-weight:300;font-size:24px;color:#fff}
.hero p{position:absolute;left:140px;width:280px;top:111px;text-align:center;font-size:9.5px;color:#fff;line-height:1.2}
.btn{position:absolute;display:flex;align-items:center;justify-content:center;font-weight:600;letter-spacing:1px}
.btn--teal{background:var(--teal);color:#fff}
.pillar{top:320px;width:130px;text-align:center}
.pillar .icon{width:48px;height:48px;margin:0 auto;border-radius:50%}
.pillar h3{margin-top:22px;font-size:12px;letter-spacing:2px;font-weight:600}
.pillar p{margin-top:14px;font-size:6.2px;line-height:1.75;color:#444}
.about{left:0;top:496px;width:560px;height:214px;background:var(--teal);color:#fff}
.about h2{position:absolute;left:230px;top:40px;font-size:16px;font-weight:500}
.about p{position:absolute;left:230px;width:225px;font-size:6.2px;line-height:1.75}
.about .mark{position:absolute;left:100px;top:88px;font-size:20px;font-weight:700;color:#7fd3c3}
.section-title{width:560px;text-align:center;font-size:16px;font-weight:500;letter-spacing:1px}
.interview{width:127px}
.interview .thumb{height:93px;position:relative;background:linear-gradient(135deg,#7a6e68,#3e3a3b)}
.interview .thumb.b{background:linear-gradient(135deg,#8a4a4a,#2e2f45)}
.interview .thumb.c{background:linear-gradient(135deg,#a0574a,#3c3434)}
.play{position:absolute;left:50%;top:50%;width:24px;height:24px;margin:-12px;border-radius:50%;background:#fff}
.play::after{content:"";position:absolute;left:9px;top:7px;border-left:8px solid #222;border-top:5px solid transparent;border-bottom:5px solid transparent}
.interview h4{margin:14px 2px 0;font-size:9.5px;font-weight:600;line-height:1.2}
.interview p{margin:10px 2px 0;font-size:6.2px;line-height:1.6;color:var(--grey)}
.pager{display:flex;gap:12px}
.pager span{width:19px;height:19px;border-radius:50%;background:#999;color:#fff;font-size:7.5px;display:flex;align-items:center;justify-content:center;border:2px solid #ddd}
.pager span.on{background:#111;border-color:#111}
.band{left:0;width:560px;background:var(--mint)}
.tab{position:absolute;height:27px;display:flex;align-items:center;justify-content:center;font-size:7.5px;font-weight:600;letter-spacing:1px}
.tab--past{width:85px;background:var(--mint-dark);color:#e8f3ec}
.tab--up{width:109px;background:#fff;color:#111}
.event{position:absolute;border-radius:3px;overflow:hidden;color:#fff;font-size:7.8px;font-weight:700;letter-spacing:.8px;line-height:1.6}
.event .cap{position:absolute;left:16px;bottom:12px;right:10px}
.event--text{background:var(--mint-dark);font-weight:400;letter-spacing:0;font-size:6.3px;line-height:1.75;padding:14px 16px}
.event--text b{font-size:7.5px;display:block;font-weight:700}
.date{position:absolute;width:194px;height:51px;background:var(--card);display:flex}
.date .day{width:51px;color:#fff;text-align:center;padding-top:9px;line-height:1}
.date .day small{display:block;font-size:12px}
.date .day strong{display:block;font-size:18px;font-weight:700}
.date .txt{padding:12px 12px;font-size:6.2px;color:#666;line-height:1.4}
.date .txt b{display:block;font-size:7.5px;color:#111;margin-bottom:2px}
.join{left:0;top:784px;width:560px;height:186px;background:var(--light);text-align:center}
.join h2{margin-top:33px;font-size:16px;font-weight:500;color:var(--teal);letter-spacing:.5px}
.join p{margin:16px auto 0;width:300px;font-size:6.2px;line-height:1.8;color:#555}
.footer{left:0;top:970px;width:560px;height:150px;background:var(--footer);color:#fff}
.footer h5{font-size:7.3px;font-weight:600;letter-spacing:.5px}
.footer p{margin-top:14px;font-size:5.6px;line-height:1.65;color:#999}
.social{display:flex;gap:7px;margin-top:12px}
.social span{width:16px;height:16px;border-radius:50%;background:#fff}
</style>
</head>
<body>

<main class="page page--left">
  <header class="abs nav">
    <div class="abs brand">Wellorivan</div>
    <nav class="abs nav-links"><span>About Wellorivan</span><span>Interviews</span><span>Events</span><span>Blogs</span><span>Social Presence</span><span>Contact</span></nav>
  </header>

  <section class="abs hero" role="img" aria-label="Group photo of smiling community members outdoors">
    <h1>Bright days with a little zest</h1>
    <p>Lorem ipsum dolor sit amet, consectetur adipisicing elit, sed do eiusmod tempor incididunt ut</p>
    <div class="btn btn--teal" style="left:234px;top:142px;width:93px;height:27px;font-size:9.5px">EXPLORE</div>
  </section>

  <div class="abs pillar" style="left:72px">
    <div class="icon" style="background:#fde3c8" role="img" aria-label="Mind icon"></div>
    <h3 style="color:var(--orange)">MIND</h3>
    <p>Lorem ipsum dolor sit amet, consectetur adipisicing elit, sed do eiusmod tempor incididunt ut labore et dolore</p>
  </div>
  <div class="abs pillar" style="left:215px">
    <div class="icon" style="background:#d6d7ee" role="img" aria-label="Movement icon"></div>
    <h3 style="color:var(--navy)">MOVEMENT</h3>
    <p>Lorem ipsum dolor sit amet, consectetur adipisicing elit, sed do eiusmod tempor incididunt ut labore et dolore</p>
  </div>
  <div class="abs pillar" style="left:358px">
    <div class="icon" style="background:#cfe9d7" role="img" aria-label="Meals icon"></div>
    <h3 style="color:var(--green)">MEALS</h3>
    <p>Lorem ipsum dolor sit amet, consectetur adipisicing elit, sed do eiusmod tempor incididunt ut labore et dolore</p>
  </div>

  <section class="abs about">
    <div class="mark">Wellorivan</div>
    <h2>ABOUT WELLORIVAN</h2>
    <p style="top:76px">Lorem ipsum dolor sit amet, consectetur adipisicing elit, sed do eiusmod tempor incididunt ut labore et dolore magna aliqua. Ut enim ad minim veniam, quis nostrud exercitation ullamco laboris nisi ut aliquip ex ea commodo consequat.</p>
    <p style="top:130px">Duis aute irure dolor in reprehenderit in voluptate velit esse cillum dolore eu fugiat nulla pariatur. Excepteur sint occaecat cupidatat non proident, sunt in culpa qui officia deserunt mollit anim id est laborum. Sed ut perspiciatis</p>
  </section>

  <h2 class="abs section-title" style="left:0;top:746px">INTERVIEWS</h2>
  <article class="abs interview" style="left:74px;top:802px">
    <div class="thumb" role="img" aria-label="Video still of an interviewee outdoors"><span class="play"></span></div>
    <h4>Lorem ipsum dolor sitam etcon sectetur</h4>
    <p>Lorem ipsum dolor sit amet, consectetur adipisicing elit, sed do eiusmod tempor</p>
  </article>
  <article class="abs interview" style="left:217px;top:802px">
    <div class="thumb b" role="img" aria-label="Video still of an award ceremony group"><span class="play"></span></div>
    <h4>Adipisicing elit, sed doei usmod tempor incidi</h4>
    <p>Lorem ipsum dolor sit amet, consectetur adipisicing elit, sed do eiusmod tempor</p>
  </article>
  <article class="abs interview" style="left:360px;top:802px">
    <div class="thumb c" role="img" aria-label="Video still of supporters at a sports event"><span class="play"></span></div>
    <h4>Dant ut labore et dolore magna aliqua</h4>
    <p>Lorem ipsum dolor sit amet, consectetur adipisicing elit, sed do eiusmod tempor</p>
  </article>
  <div class="abs pager" style="left:224px;top:997px"><span class="on">1</span><span>2</span><span>3</span><span>4</span></div>

  <section class="abs band" style="top:1053px;height:67px">
    <div class="tab tab--past" style="left:178px;top:38px">PAST EVENTS</div>
    <div class="tab tab--up" style="left:274px;top:38px">UPCOMING EVENTS</div>
  </section>
</main>

<main class="page page--right">
  <article class="abs interview" style="left:74px;top:-15px">
    <div class="thumb" role="img" aria-label="Video still of an interviewee outdoors"><span class="play"></span></div>
    <h4>Lorem ipsum dolor sitam etcon sectetur</h4>
    <p>Lorem ipsum dolor sit amet, consectetur adipisicing elit, sed do eiusmod tempor</p>
  </article>
  <article class="abs interview" style="left:217px;top:-15px">
    <div class="thumb b" role="img" aria-label="Video still of an award ceremony group"><span class="play"></span></div>
    <h4>Adipisicing elit, sed doei usmod tempor incidi</h4>
    <p>Lorem ipsum dolor sit amet, consectetur adipisicing elit, sed do eiusmod tempor</p>
  </article>
  <article class="abs interview" style="left:359px;top:-15px">
    <div class="thumb c" role="img" aria-label="Video still of supporters at a sports event"><span class="play"></span></div>
    <h4>Dant ut labore et dolore magna aliqua</h4>
    <p>Lorem ipsum dolor sit amet, consectetur adipisicing elit, sed do eiusmod tempor</p>
  </article>
  <div class="abs pager" style="left:224px;top:181px"><span class="on">1</span><span>2</span><span>3</span><span>4</span></div>

  <section class="abs band" style="top:237px;height:371px">
    <div class="tab tab--past" style="left:178px;top:38px">PAST EVENTS</div>
    <div class="tab tab--up" style="left:274px;top:38px">UPCOMING EVENTS</div>
    <div class="event" style="left:82px;top:99px;width:194px;height:118px;background:linear-gradient(180deg,#6b625c,#1a1818)" role="img" aria-label="Photo of a community talk audience">
      <div class="cap">LOREM IPSUM DOLOR SIT AMET, CONSECTETUR ADIPISICING ELIT</div>
    </div>
    <div class="event" style="left:285px;top:99px;width:194px;height:118px;background:linear-gradient(180deg,#4a4d60,#151517)" role="img" aria-label="Photo of a group outside a government building">
      <div class="cap">CONSECTETUR ADIPISICING ELITS EDO EIUSMOD TEMPOR INCIDI</div>
    </div>
    <div class="event event--text" style="left:82px;top:229px;width:143px;height:105px">
      <b>Lorem ipsum dolor sit</b>consectetur adipisicing elit, sed do eiusmod tempor incididunt ut labore et dolore magna aliqua. Ut enim ad minim veniam, quis nostrud exercitation ullamco laboris nisi ut aliquip ex ea
    </div>
    <div class="event" style="left:234px;top:229px;width:245px;height:105px;background:linear-gradient(180deg,#8c7f78,#1a1717)" role="img" aria-label="Photo of a speaker meeting community members">
      <div class="cap">CONSECTETUR ADIPISICING ELITS EDO EIUSM</div>
    </div>
  </section>

  <div class="date" style="left:82px;top:638px"><div class="day" style="background:var(--orange)"><small>JAN</small><strong>30</strong></div><div class="txt"><b>Lorem ipsum dolor sit</b>consectetur adipisicing elit, seddo eiusmod tempor incididunt</div></div>
  <div class="date" style="left:285px;top:638px"><div class="day" style="background:var(--navy)"><small>FEB</small><strong>12</strong></div><div class="txt"><b>Lorem ipsum dolor sit</b>consectetur adipisicing elit, seddo eiusmod tempor incididunt</div></div>
  <div class="date" style="left:82px;top:698px"><div class="day" style="background:var(--green)"><small>FEB</small><strong>26</strong></div><div class="txt"><b>Lorem ipsum dolor sit</b>consectetur adipisicing elit, seddo eiusmod tempor incididunt</div></div>
  <div class="date" style="left:285px;top:698px"><div class="day" style="background:var(--red)"><small>MAR</small><strong>9</strong></div><div class="txt"><b>Lorem ipsum dolor sit</b>consectetur adipisicing elit, seddo eiusmod tempor incididunt</div></div>

  <section class="abs join">
    <h2>BECOME A PART OF WELLORIVAN</h2>
    <p>Lorem ipsum dolor sit amet, consectetur adipisicing elit, sed do eiusmod tempor incididunt ut labore et dolore magna aliqua. Ut enim ad minim veniam, quis nostrud exercitation ullamco laboris nisi ut aliquip ex ea commodo consequat.</p>
    <div class="btn btn--teal" style="left:238px;top:123px;width:85px;height:27px;font-size:7.5px">GET STARTED</div>
  </section>

  <footer class="abs footer">
    <div class="abs" style="left:82px;top:35px;width:110px"><h5>ABOUT WELLORIVAN</h5><p>Lorem ipsum dolor sit amet, consectetur adipisicing elit, sed do eiusmod tempor incididunt ut labore et dolore magna aliqua. Ut enim ad minim veniam, quis</p></div>
    <div class="abs" style="left:209px;top:35px"><h5>NAVIGATION</h5><p>Interviews<br>Events<br>Blogs<br>Social Presence</p></div>
    <div class="abs" style="left:285px;top:35px"><h5>CONTACT US</h5><p>+00 111 222 3344<br>+00 111 555 6677<br><br>12 Marigold Lane, ELMBRIDGE<br>EL4 1AA<br><br>77 Saffron Row, ASHWORTH<br>AS9 3ZZ</p></div>
    <div class="abs" style="left:402px;top:35px"><h5>SOCIAL MEDIA</h5><div class="social"><span></span><span></span><span></span></div></div>
  </footer>
</main>

</body>
</html>
```